Looking for copywriting of the entire website + new selection of pictures

Hello,
My website's copy write is on the weaker side, so I'm looking for an entire re-do of my website's copy write. If you think a line is weak, re-write, otherwise you can leave it as is. We want our site to clearly explain what our events are, how they work, and why someone should sign up for them, while appealing to the hopeful, romantic, and nostalgic feelings of the visitors. Our speed dating events can be imagined as a modern day approach to the old-fashioned way of dating, where people got to know each other in person, away from the dating apps!! Additionally, I feel nearly all the existing pictures are rather weak, so please select entirely new pictures which give the website a less amateur feel, while retaining the playful nature of the brand. If there are areas where you think that section would benefit from no pictures at all, please communicate that.
Let me know if there are any further questions and thank you!
You can find the site at:
https://www.lanternmeetups.com
Industry/Entity Type
Speed Dating/Romance
Number of Pages Required
1 page
Look and feel
Each slider illustrates characteristics of the customer's brand and the style your logo design should communicate.

```html
<!DOCTYPE html>
<html lang="en">
<head>
<meta charset="UTF-8">
<title>Lantern Meetups — Speed Dating, Face to Face</title>
<link rel="stylesheet" href="https://fonts.googleapis.com/css2?family=Cinzel:wght@400;600&family=Kaushan+Script&family=Roboto:wght@400;500&display=swap">
<style>
:root{
  --hot:#f0168d;
  --rose:#e8489e;
  --blush:#f6a9cf;
  --petal:#fbd0e4;
  --mist:#f4f3fb;
  --ink:#1e1e24;
  --muted:#4a4a55;
  --frame:#2b2b33;
  --white:#ffffff;
}
*{box-sizing:border-box;margin:0;padding:0}
html,body{width:1200px;height:5025px;overflow:hidden}
body{position:relative;background:var(--white);font-family:"Roboto",sans-serif;color:var(--ink)}
.abs{position:absolute}
.serif{font-family:"Cinzel",serif;color:var(--hot);font-weight:400;letter-spacing:1px}
.btn{position:absolute;display:flex;align-items:center;justify-content:center;border-radius:22px;font-size:11px;height:32px;text-decoration:none}
.btn-solid{background:linear-gradient(90deg,var(--hot),var(--rose));color:var(--white)}
.btn-line{border:2px solid var(--hot);color:var(--hot);background:var(--white)}
.dot{position:absolute;border-radius:50%;background:var(--hot)}
.dot.soft{background:var(--petal)}
.ph{position:absolute}

/* nav */
.brand{position:absolute;left:127px;top:70px;display:flex;align-items:center;gap:10px;font-family:"Cinzel",serif;font-size:22px;color:var(--hot);font-weight:600}
.brand i{width:18px;height:18px;border-radius:50%;background:var(--hot);display:block}
.nav{position:absolute;top:49px;left:346px;font-size:11px}
.nav a{color:var(--ink);text-decoration:none;position:absolute;white-space:nowrap}
.social-dot{position:absolute;top:36px;width:34px;height:34px;border-radius:50%;background:linear-gradient(135deg,var(--hot),var(--rose))}

/* hero */
.tagline{left:124px;top:262px;font-family:"Kaushan Script",cursive;font-size:30px}
.hero-title{left:122px;top:312px;font-size:50px;white-space:nowrap}
.hero-text{left:124px;top:392px;font-size:14px;line-height:37px}
.hero-text li{list-style:none}
.hero-text li.bullet::before{content:"\2665";margin-right:6px}

/* phones */
.phone{position:absolute;border:6px solid var(--frame);background:var(--white);overflow:hidden}
.phone .status{position:absolute;top:10px;left:14px;right:14px;display:flex;justify-content:space-between;font-size:9px;color:var(--ink)}
.app-name{position:absolute;left:0;width:100%;text-align:center;font-family:"Cinzel",serif;color:var(--white);font-weight:600;line-height:1.1}
.app-btn{position:absolute;left:50%;transform:translateX(-50%);display:flex;align-items:center;justify-content:center;border-radius:20px;font-size:14px}
.app-btn.fill{background:var(--white);color:var(--hot)}
.app-btn.line{border:2px solid var(--white);color:var(--white)}
.screen-h{position:absolute;font-family:"Cinzel",serif;font-size:18px;color:var(--ink)}
.screen-s{position:absolute;font-size:11px;color:var(--ink)}
.field{position:absolute;left:22px;right:22px;border-bottom:1px solid #999;font-size:9px;padding-bottom:5px}
.tabbar{position:absolute;left:0;right:0;bottom:0;height:40px;border-top:1px solid #eee;display:flex;font-size:8px}
.tabbar span{flex:1;display:flex;flex-direction:column;align-items:center;justify-content:flex-end;padding-bottom:5px;gap:4px}
.tabbar span::before{content:"";width:12px;height:10px;border:1.5px solid #777;border-radius:2px}
.tabbar .on{background:var(--blush);color:var(--white)}
.tabbar .on::before{border-color:var(--white)}
.msg-list{position:absolute;top:86px;left:14px;list-style:none;font-size:8px}
.msg-list li{display:flex;align-items:center;gap:10px;height:40.5px}
.avatar{width:26px;height:26px;border-radius:50%;background:linear-gradient(135deg,#d6b2a6,#8e6b67);flex:none}

/* about */
.about-title{left:590px;top:735px;font-size:46px}
.about-text{left:590px;top:795px;width:450px;font-size:14px;line-height:28.5px;color:var(--muted)}

/* section titles */
.center-title{left:0;width:1200px;text-align:center;font-size:46px}
.sub{left:0;width:1200px;text-align:center;font-size:17px}

/* locations */
.loc{position:absolute;top:2607px;width:205px;height:176px;display:flex;flex-direction:column;align-items:center;justify-content:center;gap:18px;color:var(--white);font-family:"Cinzel",serif;font-size:16px}
.loc .pin{width:72px;height:72px;border-radius:50%;background:var(--white);display:flex;align-items:center;justify-content:center}

/* casual cards */
.card{position:absolute;top:3046px;width:310px;height:464px;background:var(--white);box-shadow:0 4px 18px rgba(180,100,150,.18);border-radius:4px;text-align:center}
.card .photo{position:absolute;left:12px;top:12px;width:286px;height:176px;border:2px solid var(--hot)}
.card .badge{position:absolute;left:135px;top:166px;width:40px;height:40px;border-radius:50%;background:var(--blush);border:3px solid var(--white)}
.card h3{position:absolute;top:222px;left:0;width:100%;font-size:26px;line-height:36px}
.card p{position:absolute;left:18px;right:18px;font-size:12.5px;line-height:21px;color:var(--muted)}

/* faq */
.faq-title{left:527px;top:3640px;font-size:32px}
.faq-item{position:absolute;left:523px;width:553px;height:48px;border:2px solid var(--petal);background:#fdebf4;display:flex;align-items:center;justify-content:space-between;padding:0 20px;font-size:15px}
.faq-answer{position:absolute;left:527px;top:3770px;width:545px;font-size:11.5px;line-height:19px;color:var(--muted)}

/* cta */
.cta-title{left:115px;top:4375px;font-size:50px;line-height:64px;color:var(--hot);white-space:nowrap}
.cta-sub{left:115px;top:4512px;font-size:18px;color:var(--white)}

/* footer */
.foot-h{position:absolute;top:4800px;font-family:"Cinzel",serif;font-size:18px;color:var(--hot);font-weight:400}
.foot-list{position:absolute;top:4836px;font-size:11.5px;line-height:22px;list-style:none}
.foot-list li{display:flex;align-items:flex-start;gap:8px}
.foot-list .ic{width:16px;height:16px;border-radius:50%;background:var(--hot);flex:none;margin-top:3px}
.copyright{position:absolute;left:0;top:4985px;width:1200px;text-align:center;font-size:10px;color:var(--muted);border-top:1px solid #ddd;padding-top:12px}
</style>
</head>
<body>

<svg class="abs" style="left:0;top:0" width="1200" height="5025" aria-hidden="true">
  <ellipse cx="260" cy="20" rx="250" ry="170" fill="#fbd0e4"/>
  <ellipse cx="150" cy="-20" rx="230" ry="150" fill="#f6a9cf"/>
  <path d="M0 1170 C250 1090 420 1210 700 1150 C950 1100 1100 1110 1200 1150 L1200 1950 C900 1990 600 1930 300 1960 C150 1975 50 1960 0 1950 Z" fill="#f4f3fb"/>
  <path d="M0 2940 C300 2880 600 2960 900 2900 C1050 2870 1150 2880 1200 2900 L1200 3600 C900 3650 500 3580 200 3640 C100 3660 30 3650 0 3640 Z" fill="#f4f3fb"/>
  <path d="M0 4250 C250 4220 450 4270 700 4235 C900 4210 1100 4200 1200 4230 L1200 4720 C900 4760 500 4690 200 4740 C100 4755 30 4740 0 4730 Z" fill="#f0168d"/>
  <path d="M0 4290 C300 4250 550 4320 800 4280 C1000 4250 1120 4260 1200 4280 L1200 4680 C900 4720 500 4650 200 4700 C100 4715 30 4700 0 4690 Z" fill="#f29ac6" opacity=".75"/>
</svg>

<!-- navigation -->
<div class="brand"><i></i>Lantern Meetups</div>
<nav class="nav">
  <a style="left:0">Home</a>
  <a style="left:84px">About Us</a>
  <a style="left:180px">Event Locations</a>
  <a style="left:322px">How It Works</a>
  <a style="left:440px">Faq</a>
</nav>
<span class="social-dot" style="left:848px" aria-label="Circlebook"></span>
<span class="social-dot" style="left:889px" aria-label="Clipstream"></span>
<span class="social-dot" style="left:930px" aria-label="Snapgallery"></span>
<a class="btn btn-solid" style="left:970px;top:37px;width:108px">Contact Us</a>

<!-- hero -->
<div class="abs tagline">Stop swiping. Start Dating!</div>
<h1 class="abs serif hero-title">LANTERN MEETUPS</h1>
<ul class="abs hero-text">
  <li>Speed dating the old-fashioned way: face to face, phones away.</li>
  <li class="bullet">No hosts, no name tags, just easy and genuine conversation</li>
  <li class="bullet">Pick an evening near you - meet someone new tonight</li>
</ul>
<a class="btn btn-solid" style="left:121px;top:513px;width:108px">How it Works</a>
<a class="btn btn-line" style="left:240px;top:513px;width:110px">Our Events</a>

<div class="ph" role="img" aria-label="Photo of a smiling couple embracing by the sea at golden hour, holding red roses" style="left:700px;top:78px;width:490px;height:510px;border-radius:50% 45% 50% 40%;background:radial-gradient(circle at 50% 40%,#f3c3b5,#e8a0c4 60%,#f4b7d6)"></div>
<span class="dot soft" style="left:560px;top:420px;width:90px;height:90px"></span>
<span class="dot soft" style="left:884px;top:585px;width:36px;height:36px"></span>
<div class="phone" style="left:648px;top:248px;width:168px;height:357px;border-radius:24px;background:linear-gradient(180deg,#f7b6d7,#e8489e)">
  <div class="app-name" style="top:140px;font-size:24px">Lantern<br>Meetups</div>
  <div class="app-btn fill" style="top:220px;width:118px;height:30px">Login</div>
  <div class="app-btn line" style="top:262px;width:118px;height:30px">Sign in</div>
</div>

<!-- about -->
<div class="ph" role="img" aria-label="Illustration of two clinking wine glasses with a heart" style="left:306px;top:718px;width:176px;height:176px;border-radius:6px;background:#fbc8df"></div>
<div class="ph" role="img" aria-label="Illustration of playing cards with a heart" style="left:157px;top:848px;width:122px;height:112px;border-radius:6px;background:var(--hot)"></div>
<div class="ph" role="img" aria-label="Illustration of small floating hearts" style="left:306px;top:960px;width:120px;height:114px;border-radius:6px;background:var(--blush)"></div>
<span class="dot" style="left:410px;top:680px;width:26px;height:26px"></span>
<span class="dot" style="left:128px;top:808px;width:30px;height:30px"></span>
<span class="dot" style="left:463px;top:1000px;width:30px;height:30px"></span>
<span class="dot soft" style="left:495px;top:770px;width:28px;height:28px"></span>
<span class="dot soft" style="left:196px;top:805px;width:14px;height:14px"></span>
<span class="dot soft" style="left:140px;top:890px;width:12px;height:12px"></span>
<span class="dot soft" style="left:455px;top:952px;width:14px;height:14px"></span>
<span class="dot soft" style="left:427px;top:1055px;width:14px;height:14px"></span>
<h2 class="abs serif about-title">ABOUT US</h2>
<p class="abs about-text">Remember when people met across a table instead of a screen? We are bringing that feeling back. Lantern Meetups hosts relaxed speed-dating evenings in cozy local venues, where you sit down, share a drink and enjoy a handful of short, real conversations. No endless swiping, no polished profiles - just the spark of meeting someone in person.</p>
<a class="btn btn-solid" style="left:590px;top:986px;width:106px">Learn More</a>

<!-- how it works -->
<span class="dot" style="left:500px;top:1192px;width:22px;height:22px"></span>
<span class="dot soft" style="left:303px;top:1252px;width:16px;height:16px"></span>
<span class="dot soft" style="left:236px;top:1270px;width:12px;height:12px"></span>
<span class="dot soft" style="left:890px;top:1250px;width:14px;height:14px"></span>
<h2 class="abs serif center-title" style="top:1225px">HOW IT WORKS</h2>
<p class="abs sub" style="top:1300px">Book a seat, show up, talk, then match - we keep things natural</p>

<div class="phone" style="left:238px;top:1398px;width:240px;height:500px;border-radius:22px">
  <div class="status"><span>9:41</span><span>5:30</span><span>100%</span></div>
  <div class="app-name" style="top:120px;font-size:18px;color:var(--hot)">Lantern<br>Meetups</div>
  <div class="screen-s" style="top:205px;left:0;width:100%;text-align:center">Flirt and meet new People</div>
  <div class="field" style="top:242px">Username*</div>
  <div class="field" style="top:274px">Password*</div>
  <div class="app-btn" style="top:306px;width:190px;height:14px;font-size:7px;background:var(--hot);color:var(--white)">Login</div>
  <div class="screen-s" style="top:326px;left:0;width:100%;text-align:center;font-size:8px">Forgot Password?</div>
</div>

<div class="phone" style="left:472px;top:1377px;width:258px;height:545px;border-radius:24px">
  <div class="status"><span>9:41</span><span>5:30</span><span>100%</span></div>
  <div class="screen-h" style="top:50px;left:18px">FILTER BY</div>
  <div class="abs" style="top:52px;right:18px;width:48px;height:16px;border-radius:8px;background:var(--blush);color:var(--white);font-size:8px;display:flex;align-items:center;justify-content:center">Apply</div>
  <div class="abs" style="top:74px;left:0;right:0;border-top:1px solid #ddd"></div>
  <div class="screen-s" style="top:84px;left:0;width:100%;text-align:center">Recent Connections</div>
  <svg class="abs" style="left:12px;top:160px" width="222" height="222" aria-hidden="true">
    <g fill="none" stroke="#f6a9cf" stroke-width="1.2"><circle cx="111" cy="111" r="30"/><circle cx="111" cy="111" r="52"/><circle cx="111" cy="111" r="74"/><circle cx="111" cy="111" r="98"/></g>
  </svg>
  <span class="ph avatar" role="img" aria-label="Profile photo of a recent connection" style="left:100px;top:248px;width:46px;height:46px;border:3px solid var(--white);box-shadow:0 0 0 2px var(--blush)"></span>
  <span class="ph avatar" role="img" aria-label="Profile photo of a recent connection" style="left:160px;top:190px;width:38px;height:38px;border:3px solid var(--white);box-shadow:0 0 0 2px var(--blush)"></span>
  <span class="ph avatar" role="img" aria-label="Profile photo of a recent connection" style="left:20px;top:290px;width:38px;height:38px;border:3px solid var(--white);box-shadow:0 0 0 2px var(--blush)"></span>
  <span class="ph avatar" role="img" aria-label="Profile photo of a recent connection" style="left:158px;top:344px;width:38px;height:38px;border:3px solid var(--white);box-shadow:0 0 0 2px var(--blush)"></span>
  <div class="tabbar"><span>Home</span><span class="on">Activity</span><span>Message</span></div>
</div>

<div class="phone" style="left:726px;top:1398px;width:236px;height:500px;border-radius:22px">
  <div class="status"><span>9:41</span><span>5:30</span><span>100%</span></div>
  <div class="screen-h" style="top:32px;left:0;width:100%;text-align:center;font-size:16px">MESSAGES</div>
  <div class="abs" style="top:56px;left:0;right:0;border-top:1px solid #ddd"></div>
  <div class="screen-s" style="top:64px;left:14px;font-size:9px">Recent Connections</div>
  <ul class="msg-list">
    <li><span class="avatar"></span>Jamie Morel</li>
    <li><span class="avatar"></span>Rory Pell</li>
    <li><span class="avatar"></span>Gavin Rae</li>
    <li><span class="avatar"></span>Sunny Sloane</li>
    <li><span class="avatar"></span>Trisha Pardo</li>
    <li><span class="avatar"></span>Rita Jansen</li>
    <li><span class="avatar"></span>Jamie Morel</li>
    <li><span class="avatar"></span>Rita Jansen</li>
    <li><span class="avatar"></span>Sunny Sloane</li>
  </ul>
  <div class="tabbar"><span>Home</span><span>Activity</span><span class="on">Message</span></div>
</div>
<a class="btn btn-solid" style="left:546px;top:1962px;width:106px">Join Now</a>

<!-- event locations -->
<h2 class="abs serif center-title" style="top:2052px">EVENT LOCATIONS</h2>
<div class="ph" role="img" aria-label="Dotted world map in pink with markers on event cities" style="left:156px;top:2135px;width:888px;height:460px;border-radius:40px;background:radial-gradient(ellipse at center,#fcdbe9,#fff4f9 75%)"></div>
<div class="loc" style="left:111px;background:var(--petal)"><span class="pin"><svg width="34" height="40" viewBox="0 0 24 30"><path d="M12 1C6 1 2 5.5 2 11c0 7 10 17 10 17s10-10 10-17C22 5.5 18 1 12 1z" fill="none" stroke="#f0168d" stroke-width="3"/><circle cx="12" cy="11" r="3.5" fill="none" stroke="#f0168d" stroke-width="3"/></svg></span>BOSTON,MA</div>
<div class="loc" style="left:367px;background:var(--blush)"><span class="pin"><svg width="34" height="40" viewBox="0 0 24 30"><path d="M12 1C6 1 2 5.5 2 11c0 7 10 17 10 17s10-10 10-17C22 5.5 18 1 12 1z" fill="none" stroke="#f0168d" stroke-width="3"/><circle cx="12" cy="11" r="3.5" fill="none" stroke="#f0168d" stroke-width="3"/></svg></span>PHILADELPHIA,PA</div>
<div class="loc" style="left:620px;background:var(--rose)"><span class="pin"><svg width="34" height="40" viewBox="0 0 24 30"><path d="M12 1C6 1 2 5.5 2 11c0 7 10 17 10 17s10-10 10-17C22 5.5 18 1 12 1z" fill="none" stroke="#f0168d" stroke-width="3"/><circle cx="12" cy="11" r="3.5" fill="none" stroke="#f0168d" stroke-width="3"/></svg></span>JERSEY CITY,NJ</div>
<div class="loc" style="left:874px;background:var(--hot)"><span class="pin"><svg width="34" height="40" viewBox="0 0 24 30"><path d="M12 1C6 1 2 5.5 2 11c0 7 10 17 10 17s10-10 10-17C22 5.5 18 1 12 1z" fill="none" stroke="#f0168d" stroke-width="3"/><circle cx="12" cy="11" r="3.5" fill="none" stroke="#f0168d" stroke-width="3"/></svg></span>NEW YORK CITY,NY</div>

<!-- casual is our code -->
<span class="dot" style="left:500px;top:2922px;width:22px;height:22px"></span>
<span class="dot soft" style="left:305px;top:2983px;width:14px;height:14px"></span>
<span class="dot soft" style="left:238px;top:3005px;width:11px;height:11px"></span>
<span class="dot soft" style="left:890px;top:2981px;width:14px;height:14px"></span>
<h2 class="abs serif center-title" style="top:2955px">CASUAL IS OUR CODE</h2>

<div class="card" style="left:121px">
  <div class="photo" role="img" aria-label="Photo of a couple strolling hand in hand in everyday clothes" style="background:linear-gradient(135deg,#d9c9c2,#b7a9a3)"></div>
  <span class="badge"></span>
  <h3 class="serif">CASUAL DRESS</h3>
  <p style="top:266px">Come as you are, whether that's your work clothes or your favorite sweater. What you wear says something about who you are, and that is exactly who we want your dates to meet. There's no dress code and no pressure to impress - just show up feeling comfortable and ready to enjoy the evening.</p>
</div>
<div class="card" style="left:447px">
  <div class="photo" role="img" aria-label="Photo of a couple chatting and laughing at a cafe table" style="background:linear-gradient(135deg,#c9a98a,#8b7160)"></div>
  <span class="badge"></span>
  <h3 class="serif">CASUAL<br>CONVERSATION</h3>
  <p style="top:300px">Each date is short and sweet, so skip the small talk! Jobs and hometowns can wait until you match. Instead, dive into the fun, thoughtful prompts we place on every table and discover how someone really thinks and laughs. Whatever the outcome, every date feels worthwhile.</p>
</div>
<div class="card" style="left:772px">
  <div class="photo" role="img" aria-label="Photo of a relaxed couple sitting together outdoors among greenery" style="background:linear-gradient(135deg,#b9c2a8,#8c9a7c)"></div>
  <span class="badge"></span>
  <h3 class="serif">CASUAL DATES</h3>
  <p style="top:266px">Our evenings feel less like an event and more like a night out with friends. Forget the stiff rules of traditional speed dating and the endless scroll of dating apps. Simply arrive, find your table, and enjoy getting to know someone new - the way people have always fallen for each other.</p>
</div>

<!-- faq -->
<div class="ph" role="img" aria-label="Photo of a laughing couple hugging, the woman embracing the man from behind" style="left:0;top:3637px;width:488px;height:633px;border-radius:0 60% 0 0;background:linear-gradient(160deg,#e8cfc6,#5a4a52 70%,#2d2a33)"></div>
<h2 class="abs serif faq-title">FREQUENTLY ASKED QUESTIONS</h2>
<div class="faq-item" style="top:3718px">1.How many dates will I go on?<svg width="14" height="8" viewBox="0 0 14 8"><path d="M1 1l6 6 6-6" fill="none" stroke="#555" stroke-width="1.5"/></svg></div>
<p class="faq-answer">You'll meet 8 people at every Lantern Meetups evening - enough to find real chemistry, all in one relaxed night out with no apps involved!</p>
<div class="faq-item" style="top:3828px">2.What are the rules?<svg width="14" height="8" viewBox="0 0 14 8"><path d="M1 7l6-6 6 6" fill="none" stroke="#555" stroke-width="1.5"/></svg></div>
<div class="faq-item" style="top:3897px">3.What is your cancellation / no-show policy?<svg width="14" height="8" viewBox="0 0 14 8"><path d="M1 7l6-6 6 6" fill="none" stroke="#555" stroke-width="1.5"/></svg></div>
<div class="faq-item" style="top:3966px">4.How long do I have on each date?<svg width="14" height="8" viewBox="0 0 14 8"><path d="M1 7l6-6 6 6" fill="none" stroke="#555" stroke-width="1.5"/></svg></div>
<div class="faq-item" style="top:4035px">5.I met someone I'd like to match with, now what?<svg width="14" height="8" viewBox="0 0 14 8"><path d="M1 7l6-6 6 6" fill="none" stroke="#555" stroke-width="1.5"/></svg></div>
<div class="faq-item" style="top:4104px">6.Are there breaks in-between each date?<svg width="14" height="8" viewBox="0 0 14 8"><path d="M1 7l6-6 6 6" fill="none" stroke="#555" stroke-width="1.5"/></svg></div>

<!-- cta -->
<h2 class="abs serif cta-title">OUR EVENTS FILL UP FAST.<br>DON'T MISS OUT.</h2>
<p class="abs cta-sub">Join our monthly newsletter to be first to hear about new evenings.</p>
<a class="btn btn-solid" style="left:115px;top:4578px;width:138px;box-shadow:0 2px 6px rgba(0,0,0,.15)">Join Now</a>
<div class="phone" style="left:880px;top:4240px;width:250px;height:460px;border-radius:30px;border-width:7px;background:linear-gradient(180deg,#f7b6d7,#e8489e);transform:rotate(14deg)">
  <div class="app-name" style="top:190px;font-size:32px">Lantern<br>Meetups</div>
  <div class="app-btn fill" style="top:300px;width:160px;height:40px;font-size:18px">Login</div>
  <div class="app-btn line" style="top:356px;width:160px;height:40px;font-size:18px">Sign in</div>
</div>

<!-- footer -->
<div class="abs" style="left:125px;top:4790px;display:flex;align-items:center;gap:8px;font-family:'Cinzel',serif;font-size:20px;color:var(--hot);font-weight:600"><i style="width:16px;height:16px;border-radius:50%;background:var(--hot);display:block"></i>Lantern Meetups</div>
<p class="abs" style="left:125px;top:4866px;width:220px;font-size:11px;line-height:16px">Relaxed, in-person speed dating for people who'd rather meet face to face than swipe.</p>

<h4 class="foot-h" style="left:420px">QUICK LINKS</h4>
<ul class="foot-list" style="left:420px"><li>Home</li><li>About Us</li><li>Event Locations</li><li>How It Works</li><li>Faq</li></ul>

<h4 class="foot-h" style="left:660px">CONTACT US</h4>
<ul class="foot-list" style="left:660px;width:200px">
  <li><svg class="ic" viewBox="0 0 16 16"><circle cx="8" cy="8" r="8" fill="#f0168d"/><path d="M5 4.5l1.5-.5 1 2-1 .8a5 5 0 0 0 2.7 2.7l.8-1 2 1-.5 1.5c-3.5 0-6.5-3-6.5-6.5z" fill="#fff"/></svg>(201) 555-0147</li>
  <li style="line-height:15px;margin:4px 0"><svg class="ic" viewBox="0 0 16 16"><circle cx="8" cy="8" r="8" fill="#f0168d"/><path d="M8 3.5a3 3 0 0 0-3 3c0 2.2 3 5.5 3 5.5s3-3.3 3-5.5a3 3 0 0 0-3-3z" fill="#fff"/></svg>88 Harbor Lane, Suite 4, Jersey City, NJ 07302</li>
  <li><svg class="ic" viewBox="0 0 16 16"><circle cx="8" cy="8" r="8" fill="#f0168d"/><rect x="4" y="5" width="8" height="6" fill="#fff"/><path d="M4 5l4 3 4-3" fill="none" stroke="#f0168d"/></svg>welcome@lanternmeetups.com</li>
</ul>

<h4 class="foot-h" style="left:912px">FOLLOW US</h4>
<ul class="foot-list" style="left:912px;line-height:25px">
  <li><span class="ic"></span>Circlebook</li>
  <li><span class="ic"></span>Snapgallery</li>
  <li><span class="ic"></span>Chirper</li>
  <li><span class="ic"></span>Clipstream</li>
</ul>

<p class="copyright">Copyright © 2023 Lantern Meetups. All Rights Reserved</p>

</body>
</html>
```